Paveline Ridge

Im looking for something similar to (tarvexblacktop.example) web site. I really want it to pop!
services we offer:
- Seal Coating
- Crack Filling
- Striping
- Asphalt
- Concrete
- Signage
- Road Grinding
- Grading
- Hydro Blasting
- Recycled asphalt
- Dumpster Pads
- Pressure Washing
- Wheel blocks
- Bollard installation
- Commercial Curbing
- Job site clean up
- Sweeping
- Forestry Clean up
- ADA Compliant work
- Speed bump installation and removal
- Snow removal
- Custom stair sets (Commercial)
Target Market(s)
Parking lot maintenance, asphalt repairs, road grading
Industry/Entity Type
construction, parking lot maintenance

```html
<!DOCTYPE html>
<html lang="en">
<head>
<meta charset="utf-8">
<title>Paveline Ridge — Asphalt, Paving &amp; Parking Lot Maintenance</title>
<link href="https://fonts.googleapis.com/css2?family=Montserrat:wght@700;800;900&family=Roboto:wght@400;500;700&display=swap" rel="stylesheet">
<style>
:root{
  --lime:#7cf014;
  --ink:#151515;
  --asphalt:#1b1b1b;
  --white:#ffffff;
  --mint:#f1fbe8;
}
*{box-sizing:border-box;margin:0;padding:0}
html,body{width:1200px;height:5217px;overflow:hidden}
body{font-family:'Roboto',sans-serif;color:var(--ink);background:var(--white)}
section,header,footer,.band{position:relative;width:1200px;overflow:hidden}
.abs{position:absolute}
.display{font-family:'Montserrat',sans-serif;font-weight:800;text-transform:uppercase;letter-spacing:.5px}
.center{left:0;right:0;text-align:center}
.bar{width:60px;height:4px;background:var(--lime);margin:0 auto}

/* header */
.site-header{height:101px;background:var(--white)}
.brand{left:111px;top:14px;color:#111;font-family:'Montserrat',sans-serif;font-weight:800;line-height:1}
.brand .b1{display:block;font-size:37px;letter-spacing:1px}
.brand .b2{display:block;font-size:17px;letter-spacing:12.5px;margin-top:6px}
.contact-item{top:16px;display:flex;align-items:center;gap:12px;font-size:13px;color:#555}
.contact-item b{color:#111;font-weight:500}
.icon-box{width:28px;height:24px;background:var(--lime);display:flex;align-items:center;justify-content:center;clip-path:polygon(5px 0,100% 0,calc(100% - 5px) 100%,0 100%)}
.sep{left:840px;top:18px;width:1px;height:20px;background:#ccc}
.main-nav{left:405px;top:57px;width:795px;height:44px;background:var(--asphalt);clip-path:polygon(22px 0,100% 0,100% 100%,0 100%);font-size:14px;font-weight:500;color:var(--white)}
.main-nav a{position:absolute;top:13px;color:var(--white);text-decoration:none}
.main-nav .nav-cta{left:527px;top:6px;width:153px;height:38px;background:#333;display:flex;align-items:center;justify-content:center}

/* hero */
.hero{height:574px}
.hero-photo{inset:0;background:linear-gradient(180deg,#8aa0b5 0%,#9aa3a8 22%,#6c6c68 45%,#3b3b3a 75%,#2a2a2a 100%)}
.hero-shade{inset:0;background:radial-gradient(ellipse at 50% 48%,rgba(0,0,0,.35),rgba(0,0,0,.05) 70%)}
.hero h1{top:200px;font-size:50px;color:var(--white)}
.hero p{top:266px;font-size:16px;line-height:28px;color:var(--white)}
.btn-slant{display:inline-flex;align-items:center;justify-content:center;gap:8px;font-size:14px;font-weight:700;text-transform:uppercase;clip-path:polygon(14px 0,100% 0,calc(100% - 14px) 100%,0 100%)}
.btn-lime{background:var(--lime);color:#111}
.btn-dark{background:#1a1a1a;color:var(--lime)}
.hero .btn-slant{left:519px;top:345px;width:166px;height:38px}

/* plain divider band */
.band{background:#1d1d1d}
.band::before,.band::after{content:"";position:absolute;left:0;right:0;height:2px;background:#9a9a9a}
.band::before{top:10px}
.band::after{bottom:10px}

/* dark sections */
.dark{background:radial-gradient(circle at 30% 30%,#262626,#151515 70%)}
.section-title{font-size:40px}
.serve{height:602px}
.serve .section-title{top:66px;color:var(--white)}
.serve .bar{position:absolute;left:570px;top:122px}
.place-card{top:182px;width:450px;height:324px;background:var(--white);border-radius:6px;overflow:hidden;border:3px solid #e8e8e8}
.place-card .photo{height:261px}
.place-card span{display:block;text-align:center;font-weight:700;font-size:16px;line-height:57px;color:#111;letter-spacing:.5px}

/* services */
.services{height:598px}
.services-band{left:0;top:0;width:1200px;height:371px;background:var(--lime)}
.eyebrow{left:111px;top:54px;font-size:16px;font-weight:700;color:#111}
.services h2{left:111px;top:88px;font-size:44px;line-height:47px;color:#111}
.services .lede{left:570px;top:78px;width:517px;font-size:13.5px;font-weight:400;line-height:25.5px;color:var(--white)}
.service-viewport{left:111px;top:225px;width:977px;height:360px;overflow:hidden}
.service-track{display:flex;gap:18px;width:max-content}
.service-card{position:relative;flex:0 0 313px;height:320px;background:var(--white);box-shadow:0 10px 30px rgba(0,0,0,.12);text-align:center}
.service-card svg{margin-top:30px}
.service-card h3{font-size:17px;font-weight:700;margin-top:12px;color:#111}
.service-card p{font-size:13.5px;line-height:25px;color:#8a8a8a;margin:14px 28px 0}
.learn{position:absolute;display:flex;height:30px;font-size:12px;font-weight:700;text-transform:uppercase}
.learn .label{background:#1a1a1a;color:var(--white);display:flex;align-items:center;padding:0 26px 0 20px;clip-path:polygon(10px 0,100% 0,calc(100% - 10px) 100%,0 100%)}
.learn .tail{background:var(--lime);color:#111;width:54px;margin-left:-8px;display:flex;align-items:center;justify-content:center;clip-path:polygon(10px 0,100% 0,calc(100% - 10px) 100%,0 100%)}
.service-card .learn{left:72px;top:272px}
.slide-arrow{top:278px}

/* projects */
.projects{height:872px}
.projects .section-title{top:44px;color:#111}
.projects .bar{position:absolute;left:570px;top:114px}
.tile{background:linear-gradient(160deg,#7d8a6a,#5d5a4e 60%,#3e3d38)}
.projects .btn-slant{left:503px;top:740px;width:195px;height:42px}

/* about */
.about{height:602px}
.about-eyebrow{left:111px;top:130px;display:flex;align-items:center;gap:20px;color:var(--lime);font-weight:700;font-size:17px}
.about-eyebrow i{display:block;width:54px;height:2px;background:var(--lime)}
.about h2{left:111px;top:162px;font-size:44px;color:var(--white)}
.about p{left:111px;width:510px;font-size:14px;line-height:25px;color:#cfcfcf}
.about .learn{left:111px;top:441px}
.hex{left:699px;top:81px}

/* contact */
.cta{height:334px;background:var(--lime)}
.cta h2{top:58px;font-size:34px;line-height:37px;color:#1a1a1a}
.cta p{top:152px;font-size:14px;line-height:24px;color:#4f8f18;padding:0 170px}
.cta .btn-slant{left:503px;top:227px;width:195px;height:42px}

/* blog */
.blog{height:592px}
.blog .section-title{top:58px;color:#111}
.post{top:130px;width:311px;height:470px}
.post .photo{height:168px}
.post-body{position:absolute;left:14px;top:158px;width:283px;height:203px;background:var(--white);box-shadow:0 6px 22px rgba(0,0,0,.1);border-bottom:3px solid var(--lime);padding:18px 16px 0 30px}
.post-body h3{font-size:15px;line-height:24px;font-weight:700;color:#111}
.post-body time{display:flex;align-items:center;gap:8px;font-size:13px;color:#777;margin-top:10px}
.post-body p{font-size:13px;line-height:24px;color:#999;margin-top:14px}

/* clients */
.clients{height:304px;background:var(--mint)}
.clients .section-title{top:46px;color:#111}
.client{top:126px;width:166px;height:83px;background:var(--white);border-radius:5px;box-shadow:0 4px 14px rgba(0,0,0,.08);display:flex;align-items:center;justify-content:center;gap:8px;font-size:15px;font-weight:700;color:#333}
.client i{display:block;width:12px;height:12px;border-radius:50%;background:#333}
.round-arrow{top:155px;width:26px;height:26px;border-radius:50%;background:var(--white);box-shadow:0 2px 6px rgba(0,0,0,.15);display:flex;align-items:center;justify-content:center}

/* footer */
.site-footer{height:368px;background:var(--asphalt)}
.site-footer .brand{left:111px;top:130px;color:var(--white)}
.socials{left:150px;top:220px;display:flex;gap:16px}
.socials i{display:block;width:14px;height:14px;border:2px solid var(--white);border-radius:50%}
.foot-col h4{font-size:16px;font-weight:700;color:var(--white)}
.foot-item{position:absolute;left:0;display:flex;gap:10px;font-size:12px;line-height:17px;color:#ddd}
.foot-item b{display:block;color:var(--white);font-weight:700}
.foot-links a{position:absolute;left:0;font-size:13px;color:#ddd;text-decoration:none;white-space:nowrap}
.foot-note{font-size:12px;line-height:19px;color:#ddd;width:240px;margin-top:26px}
.quote-btn{left:859px;top:205px;width:199px;height:38px;border-radius:20px;background:var(--lime);color:var(--white);font-weight:700;font-size:14px;display:flex;align-items:center;justify-content:center}
.go-up{left:1005px;top:285px;width:80px;height:19px;border-radius:10px;background:#555;color:var(--white);font-size:11px;font-weight:700;display:flex;align-items:center;justify-content:center;gap:4px}
.foot-rule{left:111px;top:314px;width:977px;height:1px;background:#3a3a3a}
.legal{top:326px;font-size:12px;color:#ddd}
</style>
</head>
<body>

<header class="site-header">
  <div class="abs brand"><span class="b1">PAVELINE</span><span class="b2">RIDGE</span></div>
  <div class="abs contact-item" style="left:590px">
    <span class="icon-box"><svg width="14" height="14" viewBox="0 0 24 24"><path fill="#111" d="M6.6 10.8a15.1 15.1 0 0 0 6.6 6.6l2.2-2.2c.3-.3.7-.4 1-.2 1.1.4 2.3.6 3.6.6.6 0 1 .4 1 1V20c0 .6-.4 1-1 1A17 17 0 0 1 3 4c0-.6.4-1 1-1h3.5c.6 0 1 .4 1 1 0 1.3.2 2.5.6 3.6.1.3 0 .7-.2 1z"/></svg></span>
    <span>Phone: <b>(555) 014 2290</b></span>
  </div>
  <div class="abs sep"></div>
  <div class="abs contact-item" style="left:853px">
    <span class="icon-box"><svg width="14" height="12" viewBox="0 0 24 20"><path fill="#111" d="M2 2h20v16H2z"/><path fill="none" stroke="#7cf014" stroke-width="2" d="M3 3l9 8 9-8"/></svg></span>
    <span>Email: <b>info@pavelineridge.example</b></span>
  </div>
  <nav class="abs main-nav">
    <a style="left:27px">Home</a>
    <a style="left:98px">About</a>
    <a style="left:171px">Our Services</a>
    <a style="left:288px">Projects</a>
    <a style="left:377px">Blog</a>
    <a style="left:438px">Contact</a>
    <a class="nav-cta">FREE ESTIMATES</a>
  </nav>
</header>

<section class="hero">
  <div class="abs hero-photo" role="img" aria-label="Yellow asphalt roller compacting fresh pavement in a parking lot with pickup trucks behind"></div>
  <div class="abs hero-shade"></div>
  <h1 class="abs center display">Paveline Ridge</h1>
  <p class="abs center">Lorem ipsum dolor sit amet, consectetur adipiscing elit, eiusmod<br>ut aliquip ex tempor labore dolore magna aliqua.</p>
  <a class="abs btn-slant btn-lime">Get Started
    <svg width="13" height="13" viewBox="0 0 16 16"><circle cx="8" cy="8" r="8" fill="#111"/><path d="M6 4.5L9.5 8 6 11.5" stroke="#7cf014" stroke-width="2" fill="none"/></svg></a>
</section>

<div class="band" style="height:41px"></div>

<section class="serve dark">
  <h2 class="abs center display section-title">We Serve In</h2>
  <div class="bar"></div>
  <div class="abs place-card" style="left:134px">
    <div class="photo" role="img" aria-label="Crew sealing the floor of a covered commercial parking garage" style="background:linear-gradient(180deg,#b9bfc0,#6d7170 55%,#3a3d3c)"></div>
    <span>COMMERCIAL</span>
  </div>
  <div class="abs place-card" style="left:616px">
    <div class="photo" role="img" aria-label="Freshly coated red brick-pattern residential driveway" style="background:linear-gradient(180deg,#c9cfd6 0%,#b44a4a 22%,#9c3a3d 60%,#7c2d30)"></div>
    <span>RESIDENTIAL</span>
  </div>
</section>

<div class="band" style="height:44px"></div>

<section class="services">
  <div class="abs services-band"></div>
  <div class="abs eyebrow">SERVICES WE OFFER</div>
  <h2 class="abs display">Paveline Ridge<br>Services</h2>
  <p class="abs lede">Lorem ipsum dolor sit amet, consectetur adipiscing elit, sed do eiusmod tempor incididunt ut labore et dolore magna aliqua. Ut enim ad minim veniam, quis nostrud exercitation ullamco laboris nisi ut aliquip ex ea commodo consequat. Duis aute irure dolor in reprehenderit in voluptate velit</p>

  <svg class="abs slide-arrow" style="left:38px" width="24" height="34" viewBox="0 0 24 34" aria-label="Previous services"><path d="M19 3L5 17l14 14" stroke="#111" stroke-width="4" fill="none"/></svg>
  <svg class="abs slide-arrow" style="left:1130px" width="24" height="34" viewBox="0 0 24 34" aria-label="Next services"><path d="M5 3l14 14L5 31" stroke="#111" stroke-width="4" fill="none"/></svg>

  <div class="abs service-viewport">
    <div class="service-track">
      <article class="service-card">
        <svg width="64" height="48" viewBox="0 0 64 48"><path d="M20 0h24l12 48H8z" fill="#111"/><rect x="30" y="6" width="4" height="9" fill="#fff"/><rect x="30" y="20" width="4" height="9" fill="#fff"/><rect x="30" y="34" width="4" height="10" fill="#fff"/></svg>
        <h3>Seal Coating</h3>
        <p>Lorem ipsum dolor sit amet, consectetur adipiscing elit, sed do eiusmod tempor incididunt ut labore et dolore laboris magna aliqua.</p>
        <a class="learn"><span class="label">Learn More</span><span class="tail">»</span></a>
      </article>
      <article class="service-card">
        <svg width="64" height="48" viewBox="0 0 64 48"><rect x="4" y="18" width="36" height="18" fill="#111"/><path d="M40 22h12l8 8v6H40z" fill="#111"/><ellipse cx="24" cy="14" rx="16" ry="10" fill="none" stroke="#111" stroke-width="4"/><circle cx="14" cy="40" r="6" fill="#111"/><circle cx="50" cy="40" r="6" fill="#111"/><circle cx="14" cy="40" r="2" fill="#fff"/><circle cx="50" cy="40" r="2" fill="#fff"/></svg>
        <h3>Concrete</h3>
        <p>Lorem ipsum dolor sit amet, consectetur adipiscing elit, sed do eiusmod tempor incididunt ut labore et dolore laboris magna aliqua.</p>
        <a class="learn"><span class="label">Learn More</span><span class="tail">»</span></a>
      </article>
      <article class="service-card">
        <svg width="64" height="48" viewBox="0 0 64 48"><rect x="20" y="0" width="24" height="30" fill="#111"/><path d="M32 6l2.5 5 5.5.8-4 3.9 1 5.5-5-2.6-5 2.6 1-5.5-4-3.9 5.5-.8z" fill="#7cf014"/><rect x="30" y="30" width="4" height="14" fill="#111"/><rect x="22" y="44" width="20" height="4" fill="#111"/></svg>
        <h3>Signage</h3>
        <p>Lorem ipsum dolor sit amet, consectetur adipiscing elit, sed do eiusmod tempor incididunt ut labore et dolore laboris magna aliqua.</p>
        <a class="learn"><span class="label">Learn More</span><span class="tail">»</span></a>
      </article>
      <article class="service-card"><h3>Crack Filling</h3><p>Sealing cracks early to stop water damage and extend pavement life.</p></article>
      <article class="service-card"><h3>Striping</h3><p>Crisp, durable line striping for lots, stalls and traffic lanes.</p></article>
      <article class="service-card"><h3>Asphalt</h3><p>New paving, overlays and patch repairs built to last.</p></article>
      <article class="service-card"><h3>Road Grinding</h3><p>Milling worn surfaces back to a clean, level base.</p></article>
      <article class="service-card"><h3>Grading</h3><p>Road and site grading for proper drainage and a solid base.</p></article>
      <article class="service-card"><h3>Hydro Blasting</h3><p>High-pressure water cleaning for tough surface prep.</p></article>
      <article class="service-card"><h3>Recycled Asphalt</h3><p>Cost-effective recycled millings for lots and access roads.</p></article>
      <article class="service-card"><h3>Dumpster Pads</h3><p>Heavy-duty concrete pads that handle daily truck loads.</p></article>
      <article class="service-card"><h3>Pressure Washing</h3><p>Clean walks, lots and building fronts in one visit.</p></article>
      <article class="service-card"><h3>Wheel Blocks</h3><p>Parking stops installed and replaced to keep lots orderly.</p></article>
      <article class="service-card"><h3>Bollard Installation</h3><p>Steel bollards that protect meters, doors and walkways.</p></article>
      <article class="service-card"><h3>Commercial Curbing</h3><p>Clean concrete curbing for commercial lots and entries.</p></article>
      <article class="service-card"><h3>Job Site Clean Up</h3><p>Leaving every site swept, hauled out and ready to use.</p></article>
      <article class="service-card"><h3>Sweeping</h3><p>Scheduled lot sweeping to keep surfaces safe and tidy.</p></article>
      <article class="service-card"><h3>Forestry Clean Up</h3><p>Brush and debris removal along roads and forest sites.</p></article>
      <article class="service-card"><h3>ADA Compliant Work</h3><p>Ramps, tactile pads and stalls that meet ADA standards.</p></article>
      <article class="service-card"><h3>Speed Bumps</h3><p>Speed bump installation and removal for safer lots.</p></article>
      <article class="service-card"><h3>Snow Removal</h3><p>Fast plowing and clearing to keep lots open all winter.</p></article>
      <article class="service-card"><h3>Custom Stair Sets</h3><p>Commercial concrete stair sets formed to fit the site.</p></article>
    </div>
  </div>
</section>

<section class="projects">
  <h2 class="abs center display section-title">Our Projects</h2>
  <div class="bar"></div>
  <div class="abs tile" style="left:111px;top:150px;width:483px;height:280px" role="img" aria-label="Compact track loader grading gravel beside a road"></div>
  <div class="abs tile" style="left:604px;top:150px;width:484px;height:280px;background:linear-gradient(180deg,#6b6a52,#5a5a50 50%,#6e6e6a)" role="img" aria-label="Yellow steel bollards installed in front of utility meters"></div>
  <div class="abs tile" style="left:116px;top:440px;width:320px;height:253px;background:linear-gradient(180deg,#c7c9c4,#9a8a5a 35%,#5e4b36 70%,#4a3a2a)" role="img" aria-label="Track loader with grading attachment on a dirt site"></div>
  <div class="abs tile" style="left:446px;top:440px;width:310px;height:253px;background:linear-gradient(160deg,#9a9a96,#7b7b78 55%,#c9b14a 58%,#7b7b78 70%)" role="img" aria-label="New concrete ramp with yellow tactile warning pad"></div>
  <div class="abs tile" style="left:766px;top:440px;width:322px;height:253px;background:linear-gradient(180deg,#d9d9d4,#a9a49a 45%,#8a8780)" role="img" aria-label="Fresh concrete entry pad at a house doorway"></div>
  <a class="abs btn-slant btn-lime">See All Project
    <svg width="13" height="13" viewBox="0 0 16 16"><circle cx="8" cy="8" r="8" fill="#111"/><path d="M6 4.5L9.5 8 6 11.5" stroke="#7cf014" stroke-width="2" fill="none"/></svg></a>
</section>

<div class="band" style="height:46px"></div>

<section class="about dark">
  <div class="abs about-eyebrow"><i></i>About Us</div>
  <h2 class="abs display">Paveline Ridge</h2>
  <p class="abs" style="top:230px">Lorem ipsum dolor sit amet, consectetur adipiscing elit, sed do eiusmod tempor incididunt ut labore et dolore magna aliqua. Ut enim ad minim veniam, quis nostrud exercitation ullamco laboris nisi</p>
  <p class="abs" style="top:316px">Sed ut perspiciatis unde omnis iste natus error sit voluptatem accusantium doloremque laudantium, totam rem aperiam, eaque ipsa quae ab illo inventore veritatis et quasi architecto beatae vitae dicta sunt explicabo.</p>
  <a class="learn"><span class="label">Learn More</span><span class="tail">»</span></a>
  <svg class="abs hex" width="389" height="446" viewBox="0 0 389 446" role="img" aria-label="Newly paved path curving through a pine forest">
    <defs><linearGradient id="forest" x1="0" y1="0" x2="0" y2="1"><stop offset="0" stop-color="#d8e2e6"/><stop offset=".35" stop-color="#3f5a34"/><stop offset=".7" stop-color="#6a7a4a"/><stop offset="1" stop-color="#595a55"/></linearGradient></defs>
    <polygon points="194.5,12 377,117 377,329 194.5,434 12,329 12,117" fill="url(#forest)"/>
    <polygon points="194.5,3 385,112.5 385,333.5 194.5,443 4,333.5 4,112.5" fill="none" stroke="#7cf014" stroke-width="4"/>
  </svg>
</section>

<div class="band" style="height:47px"></div>

<section class="cta">
  <h2 class="abs center display">Contact Us Today For A Free Estimate<br>On Our Services</h2>
  <p class="abs center">Sed ut perspiciatis unde omnis iste natus error sit voluptatem accusantium doloremque laudantium, totam rem aperiam, eaque ipsa quae ab illo inventore veritatis et quasi architecto beatae vitae dicta sunt explicabo.</p>
  <a class="abs btn-slant btn-dark">See All Project
    <svg width="13" height="13" viewBox="0 0 16 16"><circle cx="8" cy="8" r="8" fill="#7cf014"/><path d="M6 4.5L9.5 8 6 11.5" stroke="#111" stroke-width="2" fill="none"/></svg></a>
</section>

<div class="band" style="height:47px"></div>

<section class="blog">
  <h2 class="abs center display section-title">Our Blog</h2>
  <article class="abs post" style="left:111px">
    <div class="photo" role="img" aria-label="Track loader leveling ground on a rural job site" style="background:linear-gradient(180deg,#a9c2d9,#7a8a5e 45%,#6b5a3e)"></div>
    <div class="post-body"><h3>Lorem ipsum consectetur adipiscing eius mod temporelit,</h3><time><svg width="11" height="11" viewBox="0 0 12 12"><circle cx="6" cy="6" r="5" stroke="#777" fill="none" stroke-width="1.4"/><path d="M6 3v3l2 1.5" stroke="#777" fill="none"/></svg>Oct 13, 2021</time><p>Sed ut perspiciatis unde omnis iste natus error sit voluptatem accusantium doloremque laudantium,</p></div>
  </article>
  <article class="abs post" style="left:446px">
    <div class="photo" role="img" aria-label="Red brick-pattern coated lane leading to a building" style="background:linear-gradient(180deg,#b8c4cc,#3d3d3d 30%,#a54a44 55%,#8c3a36)"></div>
    <div class="post-body"><h3>Lorem ipsum consectetur adipiscing eius mod temporelit,</h3><time><svg width="11" height="11" viewBox="0 0 12 12"><circle cx="6" cy="6" r="5" stroke="#777" fill="none" stroke-width="1.4"/><path d="M6 3v3l2 1.5" stroke="#777" fill="none"/></svg>Oct 13, 2021</time><p>Sed ut perspiciatis unde omnis iste natus error sit voluptatem accusantium doloremque laudantium,</p></div>
  </article>
  <article class="abs post" style="left:780px">
    <div class="photo" role="img" aria-label="Loader with grading blade cutting a dirt road through trees" style="background:linear-gradient(160deg,#6f7a5a,#8a7654 50%,#b99a3a 80%)"></div>
    <div class="post-body"><h3>Lorem ipsum consectetur adipiscing eius mod temporelit,</h3><time><svg width="11" height="11" viewBox="0 0 12 12"><circle cx="6" cy="6" r="5" stroke="#777" fill="none" stroke-width="1.4"/><path d="M6 3v3l2 1.5" stroke="#777" fill="none"/></svg>Oct 13, 2021</time><p>Sed ut perspiciatis unde omnis iste natus error sit voluptatem accusantium doloremque laudantium,</p></div>
  </article>
</section>

<section class="clients">
  <h2 class="abs center display section-title">Our Clients</h2>
  <div class="abs round-arrow" style="left:44px"><svg width="8" height="10" viewBox="0 0 8 10"><path d="M7 0v10L0 5z" fill="#111"/></svg></div>
  <div class="abs client" style="left:118px"><i></i>Corvane Lots</div>
  <div class="abs client" style="left:318px">Hollin Brew</div>
  <div class="abs client" style="left:517px">Tessel Foods</div>
  <div class="abs client" style="left:716px">Marrow &amp; Co</div>
  <div class="abs client" style="left:914px">Westerly Stables</div>
  <div class="abs round-arrow" style="left:1127px"><svg width="8" height="10" viewBox="0 0 8 10"><path d="M1 0v10l7-5z" fill="#111"/></svg></div>
</section>

<div class="band" style="height:45px"></div>

<footer class="site-footer">
  <div class="abs brand"><span class="b1">PAVELINE</span><span class="b2">RIDGE</span></div>
  <div class="abs socials" aria-label="Social links"><i></i><i></i><i></i><i></i></div>

  <div class="abs foot-col" style="left:385px;top:75px;width:260px">
    <h4>Our Office Address</h4>
    <div class="foot-item" style="top:44px"><svg width="12" height="12" viewBox="0 0 24 24"><path fill="#7cf014" d="M6.6 10.8a15.1 15.1 0 0 0 6.6 6.6l2.2-2.2c.3-.3.7-.4 1-.2 1.1.4 2.3.6 3.6.6.6 0 1 .4 1 1V20c0 .6-.4 1-1 1A17 17 0 0 1 3 4c0-.6.4-1 1-1h3.5c.6 0 1 .4 1 1 0 1.3.2 2.5.6 3.6.1.3 0 .7-.2 1z"/></svg><div><b>Phone</b>555 014 2290</div></div>
    <div class="foot-item" style="top:96px"><svg width="12" height="10" viewBox="0 0 24 20"><rect x="1" y="1" width="22" height="18" fill="#7cf014"/><path d="M2 2l10 8 10-8" stroke="#141414" stroke-width="2" fill="none"/></svg><div><b>Email</b>office@pavelineridge.example</div></div>
    <div class="foot-item" style="top:150px"><svg width="12" height="14" viewBox="0 0 12 16"><path d="M6 0a6 6 0 0 1 6 6c0 4.5-6 10-6 10S0 10.5 0 6a6 6 0 0 1 6-6z" fill="#7cf014"/><circle cx="6" cy="6" r="2.2" fill="#141414"/></svg><div><b>Location</b>Lorem ipsum dolor sit consectetur<br>adipiscing elit,</div></div>
  </div>

  <div class="abs foot-col" style="left:697px;top:75px;width:140px">
    <h4>Company</h4>
    <div class="foot-links">
      <a style="top:45px">Home</a><a style="top:71px">About Us</a><a style="top:97px">Our Services</a>
      <a style="top:122px">Projects</a><a style="top:148px">News</a><a style="top:174px">Contact</a>
    </div>
  </div>

  <div class="abs foot-col" style="left:859px;top:75px;width:240px">
    <h4>Still have questions?</h4>
    <p class="foot-note">Contact us using this form. A representative will answer your questions as soon as possible.</p>
  </div>
  <a class="abs quote-btn">GET A QUOTE</a>
  <a class="abs go-up"><svg width="8" height="8" viewBox="0 0 8 8"><path d="M4 0l4 5H5v3H3V5H0z" fill="#fff"/></svg>Go Up</a>
  <div class="abs foot-rule"></div>
  <div class="abs legal" style="left:111px">© 2021 Paveline Ridge | All Rights Reserved</div>
  <div class="abs legal" style="right:117px">Privacy Policy &nbsp;|&nbsp; Cookie Policy &nbsp;|&nbsp; Terms Of Services</div>
</footer>

</body>
</html>
```